Refresh our Logo and Letterhead!

We would like to see designs with blue, green, teal etc. Our current logo and contact details for the letterhead is attached.
We're a small boutique firm based in Sydney, Australia. We're near the coast and not opposed to coastal images. We practice in property law and have primarily female practitioners, although we don't necessarily need the logo and letterhead to be too feminine. We would like to see designs with blue, green, teal etc. Our current logo and contact details for the letterhead is attached.
We're a small boutique firm based in Sydney, Australia. We're near the coast and not opposed to coastal images. We practice in property law and have primarily female practitioners, although we don't necessarily need the logo and letterhead to be too feminine.

Target Market(s)

Young professionals

Industry/Entity Type

Law Firm

Logo Text

Marwick Legal

Font styles to use
Serif
Sans Serif

Colors
34a7d8
00a990
85acd3
886aae

Requirements
Must have
• The letterhead must have the text in the "contact info" jpg uploaded with the brief.
Nice to have
• We'd like to see some simple, innovating, fresh ideas. A watermark or something interesting in the background would be good.

```html
<!DOCTYPE html>
<html lang="en">
<head>
<meta charset="utf-8">
<title>Marwick Legal Letterhead</title>
<link rel="stylesheet" href="https://fonts.googleapis.com/css2?family=Poppins:wght@300;400;500;600&family=Montserrat:wght@600&family=Allura&display=swap">
<style>
  :root {
    --sky: #45b8e6;
    --sky-deep: #1682b3;
    --teal: #0e8d88;
    --ink: #2b2b2b;
    --muted: #6b6b6b;
    --ground: #e9e9ea;
    --paper: #ffffff;
  }
  * { margin: 0; padding: 0; box-sizing: border-box; }
  html, body { width: 1200px; height: 1049px; overflow: hidden; }
  body {
    background: var(--ground);
    font-family: "Poppins", Arial, sans-serif;
    color: var(--ink);
  }
  .letterhead {
    position: absolute;
    left: 247px;
    top: 24px;
    width: 707px;
    height: 1000px;
    background: var(--paper);
    box-shadow: 0 6px 24px rgba(0,0,0,0.12);
    overflow: hidden;
  }
  .letterhead__bands { position: absolute; inset: 0; width: 100%; height: 100%; }
  .brand {
    position: absolute; left: 52px; top: 98px;
    display: flex; align-items: center; gap: 12px;
  }
  .brand__dot { width: 26px; height: 26px; border-radius: 50%; background: var(--sky); }
  .brand__name {
    font-weight: 400; font-size: 34px; color: var(--sky-deep);
    letter-spacing: 0.5px;
  }
  .contact {
    position: absolute; right: 34px; top: 50px;
    list-style: none; text-align: right;
    font-size: 9.5px; line-height: 1.45; color: var(--muted);
  }
  .contact__item { display: flex; align-items: flex-start; justify-content: flex-end; gap: 10px; margin-bottom: 4px; }
  .contact__icon {
    flex: none; width: 18px; height: 18px; border-radius: 50%;
    background: var(--sky); display: flex; align-items: center; justify-content: center;
  }
  .contact__icon svg { width: 10px; height: 10px; }
  .date { position: absolute; left: 420px; top: 200px; font-size: 10px; color: var(--muted); }
  .date strong { color: var(--ink); font-weight: 600; }
  .recipient { position: absolute; left: 52px; top: 232px; font-size: 10px; line-height: 1.45; color: var(--muted); font-style: normal; }
  .recipient__name { font-family: "Montserrat", sans-serif; font-weight: 600; font-size: 15px; color: var(--ink); }
  .recipient__role { font-weight: 500; color: var(--ink); }
  .salutation { position: absolute; left: 52px; top: 322px; font-size: 10.5px; font-weight: 600; }
  .body-copy {
    position: absolute; left: 52px; top: 350px; width: 600px;
    font-size: 9.6px; line-height: 1.75; color: var(--muted); font-weight: 300;
  }
  .body-copy p { margin-bottom: 12px; }
  .signoff { position: absolute; left: 52px; top: 710px; width: 190px; }
  .signoff__signature { font-family: "Allura", cursive; font-size: 38px; color: #1f2456; line-height: 1; }
  .signoff__rule { border-top: 1px solid #bbb; margin-top: 6px; padding-top: 6px; font-size: 9px; font-weight: 600; letter-spacing: 1px; }
  .firm { position: absolute; right: 52px; top: 672px; text-align: right; }
  .firm__name { font-size: 17px; font-weight: 400; color: var(--ink); }
  .firm__abn { font-size: 9.5px; color: var(--ink); }
  .firm__note { margin-top: 10px; font-size: 8.5px; line-height: 1.5; color: var(--muted); }
</style>
</head>
<body>
  <main class="letterhead">
    <svg class="letterhead__bands" viewBox="0 0 707 1000" preserveAspectRatio="none" aria-hidden="true">
      <path d="M0,0 H40 C18,10 4,24 0,44 Z" fill="var(--sky)"/>
      <path d="M330,0 C450,30 600,40 707,26 V0 Z" fill="var(--sky)"/>
      <path d="M330,0 C450,34 600,46 707,34" fill="none" stroke="var(--teal)" stroke-width="3"/>
      <path d="M0,1000 C160,940 450,930 707,860 V1000 Z" fill="var(--sky)"/>
      <path d="M0,975 C180,915 460,905 707,835" fill="none" stroke="var(--teal)" stroke-width="4"/>
    </svg>

    <header class="brand">
      <span class="brand__dot"></span>
      <span class="brand__name">Marwick Legal</span>
    </header>

    <ul class="contact">
      <li class="contact__item"><span>02 4310 2286<br>0431 558 902</span>
        <span class="contact__icon"><svg viewBox="0 0 10 10"><path d="M2 1 L4 1 L4.5 3 L3.4 3.8 C4 5 5 6 6.2 6.6 L7 5.5 L9 6 L9 8 C5 8.5 1.5 5 2 1 Z" fill="#fff"/></svg></span></li>
      <li class="contact__item"><span>02 8140 6615</span>
        <span class="contact__icon"><svg viewBox="0 0 10 10"><rect x="2" y="1" width="6" height="3" fill="#fff"/><rect x="1" y="4" width="8" height="4" rx="1" fill="#fff"/></svg></span></li>
      <li class="contact__item"><span>office@marwicklegal.com.au<br>www.marwicklegal.com.au</span>
        <span class="contact__icon"><svg viewBox="0 0 10 10"><circle cx="5" cy="5" r="4" fill="none" stroke="#fff"/><path d="M1 5 H9 M5 1 C3 3 3 7 5 9 C7 7 7 3 5 1" fill="none" stroke="#fff" stroke-width="0.8"/></svg></span></li>
      <li class="contact__item"><span>18 Harbour View Road<br>Avoca NSW 2251</span>
        <span class="contact__icon"><svg viewBox="0 0 10 10"><path d="M5 9 C2 5.5 2 4 2 3.8 A3 3 0 0 1 8 3.8 C8 4 8 5.5 5 9 Z" fill="#fff"/><circle cx="5" cy="4" r="1.1" fill="var(--sky)"/></svg></span></li>
    </ul>

    <p class="date"><strong>Date:</strong> 07-06-2020</p>

    <address class="recipient">
      To<br>
      <span class="recipient__name">Daniel Reyes</span><br>
      <span class="recipient__role">CEO, Northline Studio</span><br>
      450 Cedar Ave Suite 12<br>
      Bellevue, WA 98004
    </address>

    <p class="salutation">Respected Sir,</p>

    <section class="body-copy">
      <p>Vero primis his utin etiam oblique eos. Lorem ipsum dolor sit amet, quo dico choro ad. At eos euismod comprehensam. Assum malorum antiopam id vix, no vis suas essent possim. Ut vim utamur fierent, eum ne zril ridens ei rectram. Nostrud atomorum ius id, cu deleniti placerat nec. Placerat deseruisse eum no, has ea eros atqui persecuti.</p>
      <p>Ei alia nihil cum. Ei putent disputando per, vide veniam tacimates pro ut, dico rebum laboramus qui at. Congue fastidii consectetuer ut quo, vix nisl primis. Corrumpit vulputate has at. Alii ludus conceptam pri ei, cum facer scaevola tacimates cu, eam ut graeco expetendis. Error tibique elaboraret nam ei, cu quodsi scripserit pro, oportere deseruisse conclusionemque ei mei. Eum aeterno scripta explicari ad, ad sit nonumy petentium.</p>
      <p>Ei reque liberavisse mei. Noster qualisque intellegam mea te, in eruditi erroribus voluptatibus eam. Pri omnis aperiam disputationi no. Pro ferri diceret pertinacia cu, tempor ancillae no vix. In justo atqui expetendis duo. Est nostro petentium te, esse clita debitis no vis, petentium gubergren vix ad. In tibique salutatus nam. Vim ut discere debitis, in vel veri disputationi. Alienum suscipit atomorum pro ut, duo at rationibus instructior.</p>
      <p>Ne vis error ignota discere, nam in cetero consequat. Vis no summo tritani iudicabit, movet recteque philosophia sed ei, amet lobortis instructior cu est. Ut erat ipsum partiendo eam, eu vim quem quodsi lobortis, eam dico tincidunt no. Iuvaret placerat convenire qui ad. Vis hinc sensibus et, mei cu vidisse graecis. Prima apparaet lucilius qui ea. Te nam modo ridens epicurei. Usu nonumy posidonium id. Mazim aeterno cu his. At quot laoreet.</p>
    </section>

    <footer class="signoff">
      <div class="signoff__signature">Laura Finch</div>
      <div class="signoff__rule">DESIGNATION GOES HERE</div>
    </footer>

    <aside class="firm">
      <div class="firm__name">Marwick Legal Pty Ltd</div>
      <div class="firm__abn">ABN. 12 345 678 901</div>
      <p class="firm__note">An incorporated legal practice under the Legal Profession Act 2004 as amended.<br>Liability limited by a scheme approved under Professional Standards Legislation</p>
    </aside>
  </main>
</body>
</html>
```